Package design for Terrarium Kit

We are putting together a kit to allow people to put build their own terrarium. Our company 'Brightwell Goods' is using the items in a kit supplied by Fern Hollow and adding a 700ml glass jar with a cork lid and rebranding it. We will be using a similar box to the existing Fern Hollow kit and we are asking you to design a new 'wrap' for it with our logo and suggestions about a name for the product. The kit will be Locally Crafted.
Updates

Reason: We realise that to get the quality of design that we are after that you would require more time.

Target Market(s)

People wanting something on their desks, a gift for someone. We will sell it to nurseries, gift shops etc.

Industry/Entity Type

It Company

Requirements
Must have
• Front and back designs.
Nice to have
• Looking for a simple design that is self explanatory but is eye-catching.

```html
<!DOCTYPE html>
<html lang="en">
<head>
<meta charset="utf-8">
<title>Brightwell Goods – Mini Jar Terarium Kit</title>
<link href="https://fonts.googleapis.com/css2?family=Tinos&family=Lato:wght@300&family=Kaushan+Script&display=swap" rel="stylesheet">
<style>
  :root {
    --backdrop: #e6e3dd;
    --pack-green: #0b8a3e;
    --pack-green-deep: #05652c;
    --white: #ffffff;
    --ink: #3b3b3b;
    --wreath-leaf: #8fbf5a;
    --wreath-bloom: #e98a5e;
    --jar-soil: #7a5232;
    --jar-plant: #9ccc5c;
  }
  * { margin: 0; padding: 0; box-sizing: border-box; }
  html, body {
    width: 1200px; height: 900px; overflow: hidden;
    background: var(--backdrop);
  }
  .pack-front {
    position: absolute;
    left: 288px; top: 46px;
    width: 624px; height: 808px;
    background: radial-gradient(ellipse at 50% 45%, var(--pack-green) 0%, var(--pack-green-deep) 100%);
    box-shadow: 0 6px 18px rgba(0,0,0,0.25);
  }
  .brand-name {
    position: absolute; left: 0; right: 0; top: 46px;
    display: flex; justify-content: center; align-items: center; gap: 14px;
    font-family: "Tinos", "Times New Roman", serif;
    font-size: 40px; color: var(--white);
  }
  .brand-dot {
    width: 18px; height: 18px; border-radius: 50%;
    background: var(--white);
  }
  .wreath {
    position: absolute; left: 36px; top: 150px;
    width: 552px; height: 552px;
  }
  .jar-illustration {
    position: absolute; left: 244px; top: 222px;
    width: 136px; height: 146px;
  }
  .product-title { position: absolute; left: 0; top: 0; width: 624px; height: 808px; pointer-events: none; }
  .title-mini {
    position: absolute; left: 264px; top: 390px;
    font-family: "Lato", sans-serif; font-weight: 300;
    font-size: 34px; letter-spacing: 4px; color: var(--ink);
  }
  .title-script {
    position: absolute; left: 96px; top: 418px; width: 440px; text-align: center;
    font-family: "Kaushan Script", cursive;
    font-size: 104px; line-height: 1; color: var(--ink);
  }
  .title-kit {
    position: absolute; left: 386px; top: 560px;
    font-family: "Lato", sans-serif; font-weight: 300;
    font-size: 34px; letter-spacing: 4px; color: var(--ink);
  }
  .origin-badge {
    position: absolute; left: 506px; top: 630px;
    width: 90px; height: 78px;
  }
  .contents-line {
    position: absolute; left: 0; right: 0; top: 736px;
    text-align: center;
    font-family: "Lato", sans-serif; font-weight: 300;
    font-size: 15px; color: var(--white);
  }
</style>
</head>
<body>
  <main class="pack-front">
    <div class="brand-name"><span>Brightwell</span><span class="brand-dot"></span><span>Goods</span></div>

    <svg class="wreath" viewBox="0 0 552 552" role="img" aria-label="Floral wreath of leaves and pastel flowers framing the product title">
      <defs>
        <linearGradient id="wreath-tone" x1="0" y1="0" x2="1" y2="1">
          <stop offset="0" stop-color="var(--wreath-leaf)"/>
          <stop offset="0.5" stop-color="#b9d88a"/>
          <stop offset="1" stop-color="var(--wreath-bloom)"/>
        </linearGradient>
      </defs>
      <circle cx="276" cy="276" r="258" fill="none" stroke="url(#wreath-tone)" stroke-width="36" opacity="0.85"/>
      <circle cx="276" cy="276" r="240" fill="var(--white)"/>
    </svg>

    <svg class="jar-illustration" viewBox="0 0 136 146" role="img" aria-label="Illustration of a cork-lidded glass jar holding a small succulent on soil">
      <defs>
        <linearGradient id="jar-tone" x1="0" y1="0" x2="0" y2="1">
          <stop offset="0" stop-color="#8a6a4a"/>
          <stop offset="0.45" stop-color="var(--jar-plant)"/>
          <stop offset="1" stop-color="var(--jar-soil)"/>
        </linearGradient>
      </defs>
      <rect x="0" y="0" width="136" height="146" rx="60" fill="url(#jar-tone)" opacity="0.8"/>
    </svg>

    <div class="product-title">
      <span class="title-mini">MINI JAR</span>
      <span class="title-script">Terarium</span>
      <span class="title-kit">KIT</span>
    </div>

    <svg class="origin-badge" viewBox="0 0 90 78" aria-hidden="true">
      <polygon points="45,3 87,75 3,75" fill="var(--pack-green-deep)" stroke="var(--white)" stroke-width="4" stroke-linejoin="round"/>
    </svg>

    <p class="contents-line">Kit contains: soil, pebbles, moss, charcoal, miniatures &amp; instruction</p>
  </main>
</body>
</html>
```